Ductless Mini Split Business Website

Tall Fern Services is looking to design an eye catching educational website about installing Ductless mini splits.

Similar to this company.
https://www.kelvarocomfort.com/

```html
<!DOCTYPE html>
<html lang="en">
<head>
<meta charset="utf-8">
<title>Tall Fern Services – Ductless Experts</title>
<link href="https://fonts.googleapis.com/css2?family=Poppins:wght@400;500;600;700&family=Roboto:wght@400;500;700&display=swap" rel="stylesheet">
<style>
:root{
  --yellow:#f9d21f;
  --yellow-soft:#fbe15c;
  --ink:#1e1e1e;
  --text:#3a3a3a;
  --muted:#8a8a8a;
  --footer:#232323;
  --white:#ffffff;
}
*{box-sizing:border-box;margin:0;padding:0}
html,body{width:1200px;height:3889px;overflow:hidden}
body{position:relative;background:var(--white);font-family:"Poppins",sans-serif;color:var(--text)}
.abs{position:absolute}
.photo{position:absolute}

/* header */
.topbar{left:640px;top:0;width:560px;height:42px;background:var(--ink);clip-path:polygon(0 0,100% 0,100% 100%,40px 100%)}
.topbar span{position:absolute;right:88px;top:11px;color:var(--white);font-weight:600;font-size:15px;white-space:nowrap}
.topbar span b{color:var(--yellow)}
.brand{left:92px;top:18px;display:flex;align-items:center;gap:10px;white-space:nowrap}
.brand-dot{width:28px;height:28px;border-radius:50%;background:var(--yellow)}
.brand-name{font-size:22px;font-weight:700;color:var(--ink)}
.brand-tag{left:94px;top:72px;font-size:16px;font-weight:700;color:var(--ink);letter-spacing:.3px;white-space:nowrap}
.nav{left:415px;top:68px;display:flex;gap:7px;font-size:14px;font-weight:500;color:var(--ink);white-space:nowrap}
.nav a{color:inherit;text-decoration:none;padding:0 10px 14px;white-space:nowrap}
.nav a.active{color:var(--yellow);border-bottom:3px solid var(--yellow)}

/* hero */
.hero-img{left:642px;top:110px;width:558px;height:635px;background:linear-gradient(120deg,#e2e2e2,#cccccc 50%,#b8b8b8)}
.hero-title{left:88px;top:312px;font-size:52px;line-height:53px;font-weight:600;color:var(--ink);white-space:nowrap}
.hero-text{left:88px;top:482px;width:440px;font-size:17px;line-height:26px;color:var(--text)}
.btn-yellow{left:88px;top:552px;width:186px;height:48px;border-radius:24px;background:linear-gradient(100deg,var(--yellow),var(--yellow-soft));font-weight:600;font-size:16px;color:var(--ink);display:flex;align-items:center;justify-content:center}

/* about */
.about-block{left:0;top:778px;width:349px;height:502px;background:var(--yellow)}
.about-img{left:89px;top:847px;width:491px;height:370px;background:linear-gradient(135deg,#f3f3f3,#dcdcdc 45%,#e46b2e 60%,#f0f0f0)}
.about-title{left:645px;top:903px;font-size:42px;line-height:43px;font-weight:600;color:var(--ink);white-space:nowrap}
.about-text{left:645px;top:1041px;width:470px;font-size:15px;line-height:27px;color:var(--text)}

/* services */
.sec-title{left:0;width:1200px;text-align:center;font-weight:600;color:var(--ink)}
.help-title{top:1352px;font-size:40px}
.svc{width:245px;height:306px;top:1426px}
.svc-label{top:1696px;width:217px;height:56px;background:var(--ink);color:var(--white);font-weight:600;font-size:17px;line-height:18px;text-align:center;display:flex;align-items:center;justify-content:center}
.svc-label.hl{background:var(--yellow);color:var(--ink)}

/* why */
.why{left:0;top:1843px;width:1200px;height:470px;background:linear-gradient(100deg,#2b2b2b,#3b3836 45%,#2e2e30)}
.why-title{top:1930px;font-size:40px;line-height:45px;color:var(--white)}
.feat{top:2050px;width:330px;color:var(--white)}
.feat h3{margin-top:10px;font-size:17px;font-weight:600;white-space:nowrap}
.feat p{margin-top:8px;width:270px;font-family:"Roboto",sans-serif;font-size:13px;line-height:21px;color:#dcdcdc}

/* stand behind */
.stand-title{top:2400px;font-size:42px;line-height:44px}
.stand{top:2510px;width:331px;height:320px}
.stand-label{top:2768px;width:269px;height:62px;background:var(--white);font-size:23px;font-weight:500;color:var(--ink);display:flex;align-items:center;justify-content:center;white-space:nowrap}
.stand-label.hl{background:var(--yellow)}

/* testimonial */
.quote-title{top:2920px;font-size:42px;line-height:44px}
.stars{left:0;top:3026px;width:1200px;text-align:center;color:var(--yellow);font-size:18px;letter-spacing:6px}
.quote{top:3060px;left:270px;width:660px;text-align:center;font-family:"Roboto",sans-serif;font-weight:500;font-size:15px;line-height:26px;color:var(--text)}
.avatar{border-radius:50%}
.person{left:0;top:3242px;width:1200px;text-align:center;font-family:"Roboto",sans-serif}
.person b{display:block;color:#e3b900;font-weight:500;font-size:15px}
.person span{font-size:11px;color:var(--muted)}

/* newsletter + footer */
.footer{left:0;top:3432px;width:1200px;height:457px;background:var(--footer)}
.news{left:89px;top:3356px;width:1022px;height:130px;background:var(--yellow)}
.news-title{left:170px;top:3392px;font-size:38px;font-weight:600;color:var(--ink);line-height:40px}
.news-sub{left:171px;top:3434px;font-size:15px;font-weight:500;color:var(--ink)}
.email{left:560px;top:3406px;width:368px;height:44px;background:var(--white);font-size:13px;color:var(--text);padding:13px 22px}
.sub{left:928px;top:3406px;width:125px;height:44px;background:var(--ink);color:var(--white);font-weight:600;font-size:15px;display:flex;align-items:center;justify-content:center}
.fcol{top:3552px;font-family:"Roboto",sans-serif;color:#a9a9a9;font-size:12.5px;line-height:20px}
.fcol h4{font-size:19px;font-weight:600;color:var(--white);margin-bottom:14px;white-space:nowrap}
.fcol li{list-style:none;display:flex;align-items:center;gap:10px;white-space:nowrap}
.fcol .ic{color:var(--yellow);width:12px;display:inline-block}
.links .ic{color:#888}
.post{display:flex;gap:16px;margin-bottom:12px}
.post .th{width:70px;height:70px;flex:none;background:linear-gradient(135deg,#bfc6cf,#6c737c)}
.post b{display:block;color:var(--white);font-weight:500;font-size:15px;white-space:nowrap}
.post em{font-style:normal;color:var(--yellow);font-size:11px}
.gal{display:grid;grid-template-columns:repeat(3,70px);gap:10px}
.gal div{height:70px;background:linear-gradient(135deg,#dfe3e7,#8f98a2)}
.viewmore{color:var(--yellow);font-weight:700;font-size:12px;margin-top:8px}
.rule{left:88px;top:3834px;width:1024px;height:1px;background:#3a3a3a}
.copy{left:0;top:3852px;width:1200px;text-align:center;font-family:"Roboto",sans-serif;font-size:12.5px;color:#e6e6e6}
.totop{left:1136px;top:3816px;width:28px;height:28px;border-radius:50%;background:var(--yellow)}
</style>
</head>
<body>

<div class="abs topbar"><span><b>&#9990;</b> Call Us Today 123-456-7891</span></div>
<div class="abs brand"><span class="brand-dot"></span><span class="brand-name">Tall Fern Services</span></div>
<div class="abs brand-tag">DUCTLESS EXPERTS</div>
<nav class="abs nav">
  <a class="active">Home</a><a>About Us</a><a>Heat Pumps</a><a>Tall Fern FAQ</a><a>Financing</a><a>Reviews</a><a>Contact Us</a>
</nav>

<div class="photo hero-img" role="img" aria-label="Wall-mounted ductless mini split unit on a grey wall"></div>
<h1 class="abs hero-title">Welcome to<br>Tall Fern Services<br>Ductless Experts</h1>
<p class="abs hero-text">Lorem Ipsum is simply dummy text of the printing and typesetting industry.</p>
<div class="abs btn-yellow">CONTACT US</div>

<div class="abs about-block"></div>
<div class="photo about-img" role="img" aria-label="Technician in orange uniform servicing an indoor mini split"></div>
<h2 class="abs about-title">Helping Portland<br>&amp; Surrounding Areas<br>Go Ductless</h2>
<p class="abs about-text">Lorem Ipsum is simply dummy text of the printing and typesetting industry lorem Ipsum has been the industry's standard dummy text ever since the 1500s, when an unknown printer took a galley of type and scrambled it to make a type specimen book. It has survived not only five centuries,</p>

<h2 class="abs sec-title help-title">How Can We Help You?</h2>
<div class="photo svc" style="left:89px;background:linear-gradient(135deg,#1d2a45,#6c7a8c 55%,#e7e7e7)" role="img" aria-label="Technician cleaning a mini split"></div>
<div class="photo svc" style="left:348px;background:linear-gradient(135deg,#8f9399,#c9ccd0 45%,#e98a28 70%,#b9bcc0)" role="img" aria-label="Installer reading refrigerant gauges"></div>
<div class="photo svc" style="left:607px;background:linear-gradient(160deg,#f4f4f4,#e2e2e2 40%,#2f3336 70%,#d8d8d8)" role="img" aria-label="Technician repairing an indoor unit"></div>
<div class="photo svc" style="left:866px;background:linear-gradient(135deg,#e6e4de,#b7b2a6 50%,#6a6356)" role="img" aria-label="Cleaning outdoor condenser coils"></div>
<div class="abs svc-label" style="left:102px">Tall Fern<br>Maintenance</div>
<div class="abs svc-label" style="left:362px">Tall Fern<br>Installation</div>
<div class="abs svc-label hl" style="left:620px">Tall Fern<br>Reapirs</div>
<div class="abs svc-label" style="left:881px">Tall Fern<br>Warranty</div>

<section class="abs why" role="img" aria-label="Dark-toned photo of a technician at work"></section>
<h2 class="abs sec-title why-title">Why Choose Tall Fern<br>Service</h2>
<div class="abs feat" style="left:131px">
  <svg width="58" height="66" viewBox="0 0 58 66" fill="none" stroke="#f9d21f" stroke-width="2.5"><path d="M4 2h34l12 12v50H4z"/><path d="M12 18h26M12 28h26M12 38h14"/><circle cx="42" cy="52" r="9"/><path d="M38 52l3 3 6-6"/></svg>
  <h3>0% Financing for 60 months</h3>
  <p>Lorem Ipsum is simply dummy text of the printing and typesetting industry lorem Ipsum has been the industry's .</p>
</div>
<div class="abs feat" style="left:450px">
  <svg width="66" height="66" viewBox="0 0 66 66" fill="none" stroke="#f9d21f" stroke-width="2.5"><circle cx="33" cy="33" r="30"/><circle cx="33" cy="33" r="20"/></svg>
  <h3>365 Day, Money Back Guarantee</h3>
  <p>Lorem Ipsum is simply dummy text of the printing and typesetting industry lorem Ipsum has been the industry's .</p>
</div>
<div class="abs feat" style="left:814px">
  <svg width="58" height="66" viewBox="0 0 58 66" fill="none" stroke="#f9d21f" stroke-width="2.5"><circle cx="26" cy="18" r="11"/><path d="M12 14h28"/><path d="M6 64V46c0-8 8-14 20-14s20 6 20 14v18"/></svg>
  <h3>We Are the Experts</h3>
  <p>Lorem Ipsum is simply dummy text of the printing and typesetting industry lorem Ipsum has been the industry's .</p>
</div>

<h2 class="abs sec-title stand-title">We Stand Behind Our<br>Tall Fern Services</h2>
<div class="photo stand" style="left:89px;background:linear-gradient(135deg,#f2f2f2,#dcdcdc 50%,#d9a98f)" role="img" aria-label="Hand holding a remote control"></div>
<div class="photo stand" style="left:435px;background:linear-gradient(135deg,#5c3f28,#b9c4a8 45%,#3c4a60)" role="img" aria-label="Cash being handed over a table"></div>
<div class="photo stand" style="left:779px;background:linear-gradient(160deg,#faf8f2,#e4dfcf 60%,#8b7d63)" role="img" aria-label="Mini split mounted near the ceiling"></div>
<div class="abs stand-label" style="left:97px">Get Some Answers</div>
<div class="abs stand-label hl" style="left:444px">Our Financing Options</div>
<div class="abs stand-label" style="left:788px">Stay up to date</div>

<h2 class="abs sec-title quote-title">Oh, my gosh!<br>These guys are awesome.</h2>
<div class="abs stars">★★★★★</div>
<p class="abs quote">Sed ut perspiciatis unde omnis iste natus error sit voluptatem accusantium doloremque laudantium, totam rem aperiam, eaque ipsa quae ab illo inventore veritatis et quasi architecto beatae vitae dicta sunt explicabo.</p>
<div class="photo avatar" style="left:461px;top:3164px;width:62px;height:62px;background:#d8cdc6;opacity:.7" role="img" aria-label="Customer portrait"></div>
<div class="photo avatar" style="left:558px;top:3154px;width:84px;height:84px;background:#b4684a" role="img" aria-label="Customer portrait"></div>
<div class="photo avatar" style="left:674px;top:3164px;width:62px;height:62px;background:#d8cdc6;opacity:.7" role="img" aria-label="Customer portrait"></div>
<div class="abs person"><b>Marla Quintero</b><span>Web Designer</span></div>

<footer class="abs footer"></footer>
<div class="abs news"></div>
<h2 class="abs news-title">Newsletter</h2>
<div class="abs news-sub">Subscribe to our newsletter</div>
<div class="abs email">Email Address</div>
<div class="abs sub">Subscribe</div>

<div class="abs fcol" style="left:88px;width:320px">
  <h4>About Us</h4>
  <p>Lorem Ipsum is simply dummy text of the printing and typesetting industry. Lorem Ipsum has been the industry's standard dummy text ever since .</p>
  <ul style="margin-top:4px;line-height:30px">
    <li><span class="ic">&#8962;</span>Some goes address here</li>
    <li><span class="ic">&#9990;</span>+555 ( 4578 ) 445</li>
    <li><span class="ic">&#9993;</span>info@email.com</li>
    <li><span class="ic">&#9679;</span>www.example.com</li>
  </ul>
</div>
<div class="abs fcol" style="left:428px;width:260px">
  <h4>Recent Posts</h4>
  <div class="post"><div class="th" role="img" aria-label="Post thumbnail"></div><div><b>Lives in a worldest</b>The lady met this fellows.<br><em>On January 18, 2017</em></div></div>
  <div class="post"><div class="th" role="img" aria-label="Post thumbnail"></div><div><b>App launches the last</b>The lady met this fellows.<br><em>On January 18, 2017</em></div></div>
</div>
<div class="abs fcol links" style="left:708px;width:160px">
  <h4>Explore Links</h4>
  <ul style="line-height:26px;color:#8d8d8d">
    <li><span class="ic">&#10148;</span>Home</li>
    <li><span class="ic">&#10148;</span>About Us</li>
    <li><span class="ic">&#10148;</span>Services</li>
    <li><span class="ic">&#10148;</span>Why Choose</li>
    <li><span class="ic">&#10148;</span>Testimonials</li>
    <li><span class="ic">&#10148;</span>Latest News</li>
    <li><span class="ic">&#10148;</span>Contact Us</li>
  </ul>
</div>
<div class="abs fcol" style="left:884px;width:240px">
  <h4>Flicker Gallery</h4>
  <div class="gal" role="img" aria-label="Gallery of installation photos"><div></div><div></div><div></div><div></div><div></div><div></div></div>
  <div class="viewmore">VIEW MORE &nbsp;»</div>
</div>
<div class="abs rule"></div>
<div class="abs copy">Copyright 2019 | All Rights Reserved</div>
<div class="abs totop"><svg width="28" height="28" viewBox="0 0 28 28"><path d="M9 16l5-5 5 5" fill="none" stroke="#1e1e1e" stroke-width="2"/></svg></div>

</body>
</html>
```